The Duchess of Nestwares is an online store specialising in all things for the home Bathroom, Kitchen,

I need a business card designed that is professional and elegant, yet not conservative. We will be wanting to brand the entire business and will have videos made where we will be interacting with the product, testing the products and basically creating an online interactive community for all those people interested in all things to do with the Home and the activities that take place in and around the home.

Target Market(s)

30-65yr old Men and Women who LOVE their Home and see it as their primary place of Happiness, their sanctuary!

Industry/Entity Type

Business

Contact Information for Business Card

www.duchessofnestwares.example The Duchess Of Nestwares-PO Box 58391, Mt Ferndale, Auckland. NEW ZEALAND. info@duchessofnestwares.example
Adore your nest! Lorraine Becker-Duponte

Font styles to use
Decorative
Script

Colors
9bcb3b
33b8a4
85cae6
b7a5cd
eda3c7
e667a6
d2a4cc
fdf9cf
fee18a

Requirements
Must have
• Attractive colours. Must feel Elegant, yet simple. A font that is rounded without sharp edges. Organic feel to the card, something raw with texture.
Nice to have
• I like the logo deign that I gave in the photos, something feminine, but fun.
Should not have
• I dont like sharp edges, or linear design. I like organic, flowing, fractal type design. Something that looks beautiful in form when you look at it.

```html
<!DOCTYPE html>
<html lang="en">
<head>
<meta charset="utf-8">
<title>The Duchess of Nestwares – Business Card</title>
<link rel="stylesheet" href="https://fonts.googleapis.com/css2?family=Roboto:wght@300;400;500&family=Roboto+Condensed:wght@500;700&display=swap">
<style>
  :root {
    --canvas-bg: #e8e8e6;
    --card-paper: #f1eff0;
    --card-shadow: rgba(0, 0, 0, 0.12);
    --accent-blue: #3a8fc1;
    --ink: #3f3f42;
  }
  * { box-sizing: border-box; margin: 0; padding: 0; }
  html, body {
    width: 966px;
    height: 1200px;
    overflow: hidden;
    background: var(--canvas-bg);
  }
  .canvas {
    position: relative;
    width: 966px;
    height: 1200px;
  }
  .card {
    position: absolute;
    left: 198px;
    width: 570px;
    height: 345px;
    background: var(--card-paper);
    box-shadow: 0 6px 18px var(--card-shadow), 0 1px 3px var(--card-shadow);
    display: flex;
    flex-direction: column;
    align-items: center;
    text-align: center;
  }
  .card--contact { top: 140px; padding-top: 118px; }
  .card--brand { top: 770px; padding-top: 148px; }

  .contact__name {
    font-family: "Roboto Condensed", sans-serif;
    font-weight: 700;
    font-size: 21px;
    letter-spacing: 0.3px;
    color: var(--accent-blue);
    text-transform: uppercase;
  }
  .contact__email,
  .contact__address,
  .contact__web {
    font-family: "Roboto", sans-serif;
    font-weight: 400;
    color: var(--ink);
    font-size: 14px;
    line-height: 1.25;
  }
  .contact__email { margin-top: 2px; }
  .contact__address { margin-top: 16px; }
  .contact__web { margin-top: 18px; letter-spacing: 0.6px; }

  .brand__name {
    font-family: "Roboto", sans-serif;
    font-weight: 400;
    font-size: 30px;
    letter-spacing: 1px;
    color: var(--ink);
    line-height: 1.15;
  }
  .brand__tagline {
    margin-top: 92px;
    font-family: "Roboto", sans-serif;
    font-weight: 500;
    font-size: 13px;
    letter-spacing: 11px;
    color: var(--ink);
    text-transform: uppercase;
  }
</style>
</head>
<body>
  <main class="canvas">
    <section class="card card--contact" aria-label="Business card contact side">
      <h1 class="contact__name">Lorraine Becker-Duponte</h1>
      <p class="contact__email">info@duchessofnestwares.example</p>
      <p class="contact__address">The Duchess Of Nestwares, PO Box 58391<br>Mt Ferndale, Auckland. NEW ZEALAND.</p>
      <p class="contact__web">www.duchessofnestwares.example</p>
    </section>

    <section class="card card--brand" aria-label="Business card brand side">
      <h2 class="brand__name">The Duchess of Nestwares</h2>
      <p class="brand__tagline">Adore your nest!</p>
    </section>
  </main>
</body>
</html>
```